Brolga Ridge Earthmoving & Transport Business Card

Can you please design a business card for an Earthworks, Haulage truck and machinery hire company. They also provide sand soil and mulch supply, as well as screening of products. Can you re-create the logo from the attached but add Brolga Ridge Earthmoving & Transport just use the three diamond design.

Target Market(s)

Earthmoving and Transport, Landscapers, Construction

Contact Information for Business Card

ABN 52 907 338 214, Dale Pettigrew, Managing Director, Brolga Ridge Earthmoving & Transport Mobile 0438 256 904 Email brgtransport2011@haulmail.example

Font styles to use
Sans Serif

Colors
ec1f27
000000
cbcbcb
ffffff

Requirements
Must have
• Listed on the back, Earthworks | Haulage | Truck and Machinery Hire | Sand, Soil & Mulch Supply | Screening of Products
Nice to have
• Would be good for it to look appealing to a mans man, because it relates to heavy machinery, earthworks, construction etc. Black, red and white would be good maybe with a bit of silver somewhere.
Should not have
• not sure

```html
<!DOCTYPE html>
<html lang="en">
<head>
<meta charset="utf-8">
<title>Brolga Ridge Earthmoving &amp; Transport – Business Card</title>
<link rel="stylesheet" href="https://fonts.googleapis.com/css2?family=Lato:wght@400;700;900&family=Montserrat:wght@500;600;700&display=swap">
<style>
  :root {
    --red: #ec1f27;
    --black: #000000;
    --ink: #141414;
    --silver: #cbcbcb;
    --white: #ffffff;
    --backdrop: #a9a9a9;
  }
  * { box-sizing: border-box; margin: 0; padding: 0; }
  html, body { width: 1200px; height: 1200px; overflow: hidden; }
  body {
    background: var(--backdrop);
    font-family: "Lato", sans-serif;
    position: relative;
  }
  .card {
    position: absolute;
    left: 150px;
    width: 900px;
    height: 515px;
    background: var(--white);
    border-radius: 26px;
    overflow: hidden;
    box-shadow: 0 10px 28px rgba(0,0,0,.25);
  }
  .card--back { top: 55px; }
  .card--front { top: 630px; }

  /* Brand mark: plain name with a single square */
  .brand {
    display: flex;
    align-items: center;
    gap: 18px;
  }
  .brand__square {
    width: 54px; height: 54px;
    background: var(--red);
    flex: none;
  }
  .brand__name {
    font-family: "Montserrat", sans-serif;
    font-weight: 600;
    color: var(--red);
    text-transform: uppercase;
    line-height: 1.15;
  }

  /* Back */
  .card--back .brand {
    position: absolute;
    left: 0; right: 0; top: 150px;
    justify-content: center;
  }
  .card--back .brand__name { font-size: 30px; letter-spacing: .5px; }
  .services {
    position: absolute;
    left: 0; right: 0; top: 345px;
    text-align: center;
    font-size: 22px;
    font-weight: 700;
    color: var(--ink);
    line-height: 1.35;
  }
  .back-edge {
    position: absolute;
    left: 0; right: 0; bottom: 0;
    height: 16px;
    background: var(--red);
  }

  /* Front */
  .person {
    position: absolute;
    left: 60px; top: 120px;
  }
  .person__name {
    font-family: "Montserrat", sans-serif;
    font-weight: 700;
    font-size: 40px;
    color: var(--black);
    text-transform: uppercase;
    letter-spacing: -.5px;
  }
  .person__role {
    font-family: "Montserrat", sans-serif;
    font-weight: 500;
    font-size: 20px;
    color: var(--red);
    text-transform: uppercase;
    margin-top: 2px;
  }
  .card--front .brand {
    position: absolute;
    right: 50px; top: 80px;
    width: 390px;
  }
  .card--front .brand__name { font-size: 24px; }
  .wave {
    position: absolute;
    inset: 0;
    width: 100%; height: 100%;
  }
  .contact {
    position: absolute;
    left: 110px; top: 385px;
    color: var(--white);
    font-size: 18px;
    line-height: 1.3;
  }
  .contact__line { display: flex; align-items: center; gap: 12px; }
  .contact__line--big { font-size: 22px; }
  .contact svg { width: 20px; height: 20px; flex: none; }
</style>
</head>
<body>

<section class="card card--back" aria-label="Card back">
  <div class="brand">
    <span class="brand__square"></span>
    <span class="brand__name">Brolga Ridge<br>Earthmoving &amp; Transport</span>
  </div>
  <p class="services">
    Earthworks | Haulage<br>
    Truck and Machinery Hire | Sand, Soil &amp; Mulch Supply | Screening of Products
  </p>
  <div class="back-edge"></div>
</section>

<section class="card card--front" aria-label="Card front">
  <svg class="wave" viewBox="0 0 900 515" preserveAspectRatio="none" aria-hidden="true">
    <path d="M0,515 L0,372 C190,300 420,318 610,312 C760,306 860,268 900,215 L900,515 Z" fill="var(--ink)"/>
    <path d="M0,366 C190,294 420,312 610,306 C760,300 860,262 900,209" fill="none" stroke="var(--silver)" stroke-width="7"/>
    <path d="M0,355 C190,282 420,300 610,294 C760,288 850,250 880,212" fill="none" stroke="var(--red)" stroke-width="5"/>
  </svg>

  <div class="person">
    <h1 class="person__name">Dale Pettigrew</h1>
    <p class="person__role">Managing Director</p>
  </div>

  <div class="brand">
    <span class="brand__square"></span>
    <span class="brand__name">Brolga Ridge<br>Earthmoving &amp; Transport</span>
  </div>

  <div class="contact">
    <p class="contact__line">ABN 52 907 338 214</p>
    <p class="contact__line">Brolga Ridge Earthmoving &amp; Transport</p>
    <p class="contact__line contact__line--big">
      <svg viewBox="0 0 24 24" aria-hidden="true"><path fill="var(--white)" d="M6.6 10.8a15.1 15.1 0 0 0 6.6 6.6l2.2-2.2c.3-.3.7-.4 1-.2 1.1.4 2.3.6 3.6.6.6 0 1 .4 1 1V20c0 .6-.4 1-1 1A17 17 0 0 1 3 4c0-.6.4-1 1-1h3.5c.6 0 1 .4 1 1 0 1.3.2 2.5.6 3.6.1.3 0 .7-.2 1z"/></svg>
      0438 256 904
    </p>
    <p class="contact__line contact__line--big">
      <svg viewBox="0 0 24 24" aria-hidden="true"><rect x="2" y="5" width="20" height="14" fill="none" stroke="var(--white)" stroke-width="2"/><path d="M2 5l10 8 10-8" fill="none" stroke="var(--white)" stroke-width="2"/></svg>
      brgtransport2011@haulmail.example
    </p>
  </div>
</section>

</body>
</html>
```